Bright Polish Leaflet Campaign

We require an eye catching double sided leaflet which is for residential properties as a marketing tool to gain more business.
If you look at our website www.brightpolishteam.example then it may help you with more information of what we are about.

We require one side of the leaflet for our (Domestic Cleaning) Services, then the other side of the leaflet for our (Carpet and Upholstery Cleaning) Service.

The Domestic Cleaning Service Side: The services we offer are weekly, fortnightly, monthly. One Off Deep Cleans. Holiday cover provided. We also have a comprehensive insurance. You may want to use our company bullet point provided in pdf which will make it stand out and outline what we do e.g.:
-Weekly, fortnightly and Monthly Cleaning Service
-Deep Blitz Cleaning
-Covered by a Comprehensive Insurance
-Carpet and Upholstery Cleaning (see overleaf)

The Carpet and Upholstery Cleaning on the other side of the leaflet has to be eye catching!

Again use bullet points along the lines of:
-Stain Removal Specialists
-Quick Drying Time
-Fresh Deodorising Finish
-Eco Friendly

Both sides of the leaflet need a call to action eg. Call Today! Our company Telephone number which should be on the leaflet in bold is 01632 960 718 .The company email which should aslo be on there is info@brightpolishco.example and the website which is not live yet is www.brightpolishco.example. If you would like to add our company accreditations they are on the website and I have attached them also.

Target Market(s)

Domestic Households- Middle aged people In York United Kingdom

Industry/Entity Type

House Cleaning

Font styles to use
Serif
Sans Serif

Requirements
Must have
• -1 Side about Domestic Cleaning Services
• -1 Side about Carpet and Upholstery Cleaning
• -Bullet points with key points
• -Phone number/website/email address
• -Logo
Nice to have
• -BE CREATIVE, USE YOUR IMAGINATION AND CREATE EYE CATCHING MATERIAL.
• -Nice to have a background colour which goes nicely with the logo our company.
Should not have
• -Not to have pink in the leaflet or yellow as it doesn't show up well I don't believe. Up to the designer as I like to give you freedom to create something amazing.

```html
<!DOCTYPE html>
<html lang="en">
<head>
<meta charset="utf-8">
<title>Bright Polish Leaflet – Front and Back</title>
<link rel="stylesheet" href="https://fonts.googleapis.com/css2?family=Open+Sans:wght@400;600;700&display=swap">
<style>
  :root {
    --brand-blue: #1f9ad6;
    --ink: #333a40;
    --bar-grey: #8e9094;
    --page: #ffffff;
    --backdrop: #e9ecef;
    --photo-bath-a: #dfeef7;
    --photo-bath-b: #9fc6df;
    --photo-person-a: #c9b8a8;
    --photo-person-b: #e8e4dc;
    --photo-trolley-a: #d8dde3;
    --photo-trolley-b: #5a86c2;
    --photo-carpet-a: #d9c4ad;
    --photo-carpet-b: #b59a80;
    --photo-room-a: #efe9df;
    --photo-room-b: #a8a39b;
    --photo-child-a: #f3efe8;
    --photo-child-b: #c8b6a0;
    --card-grey: #d7d9dc;
    --badge-blue: #2c3f8f;
  }
  * { box-sizing: border-box; margin: 0; padding: 0; }
  html, body { width: 1200px; height: 858px; overflow: hidden; }
  body {
    background: var(--backdrop);
    font-family: "Open Sans", Arial, sans-serif;
    color: var(--ink);
    position: relative;
  }
  .leaflet {
    position: absolute;
    top: 67px;
    width: 512px;
    height: 724px;
    background: var(--page);
    overflow: hidden;
    box-shadow: 0 4px 14px rgba(0,0,0,0.18);
  }
  .leaflet--front { left: 65px; }
  .leaflet--back { left: 632px; }
  .leaflet__art { position: absolute; inset: 0; width: 512px; height: 724px; }

  .brand {
    position: absolute;
    display: flex;
    align-items: center;
    gap: 8px;
    color: var(--brand-blue);
    font-weight: 700;
    line-height: 0.95;
  }
  .brand__dot {
    width: 14px; height: 14px; border-radius: 50%;
    background: var(--brand-blue);
    flex: none;
  }
  .leaflet--front .brand { left: 30px; top: 30px; font-size: 42px; }
  .leaflet--back .brand { left: 42px; top: 415px; font-size: 34px; }

  .service { position: absolute; }
  .service__title {
    color: var(--brand-blue);
    font-weight: 600;
    line-height: 24px;
    white-space: nowrap;
  }
  .service__list { list-style: none; }
  .service__item {
    display: flex;
    align-items: flex-start;
    gap: 12px;
    line-height: 21px;
    color: var(--ink);
    white-space: nowrap;
  }
  .tick { width: 30px; height: 22px; flex: none; }

  .leaflet--front .service { left: 250px; top: 478px; width: 262px; }
  .leaflet--front .service__title { font-size: 19px; margin-left: 23px; margin-bottom: 14px; }
  .leaflet--front .service__item { font-size: 15.5px; margin-bottom: 19px; }
  .leaflet--front .service__item:last-child { margin-bottom: 0; }

  .leaflet--back .service { left: 261px; top: 290px; width: 251px; }
  .leaflet--back .service__title { font-size: 20px; margin-bottom: 22px; }
  .leaflet--back .service__item { font-size: 16.5px; margin-bottom: 32px; }
  .leaflet--back .service__item:last-child { margin-bottom: 0; }

  .call {
    position: absolute;
    left: 10px;
    display: flex;
    align-items: center;
    gap: 6px;
    color: var(--brand-blue);
    font-weight: 600;
    font-size: 33px;
    line-height: 40px;
    letter-spacing: -0.3px;
  }
  .call__icon { width: 34px; height: 30px; }
  .leaflet--front .call { top: 626px; }
  .leaflet--back .call { top: 516px; }

  .rule {
    position: absolute;
    left: 0; right: 0; height: 3px;
    background: var(--brand-blue);
  }
  .leaflet--front .rule { top: 669px; }
  .leaflet--back .rule { top: 558px; }

  .contact-bar {
    position: absolute;
    left: 0; right: 0;
    height: 52px;
    background: var(--bar-grey);
    color: #fff;
    display: flex;
    align-items: center;
    justify-content: space-between;
    padding: 0 12px;
  }
  .leaflet--front .contact-bar { bottom: 0; height: 50px; }
  .leaflet--back .contact-bar { top: 563px; }
  .contact-bar__phone { font-size: 29px; font-weight: 600; letter-spacing: 0.3px; }
  .contact-bar__lines { font-size: 13px; line-height: 1.3; letter-spacing: 0.4px; }

  .accreditations {
    position: absolute;
    left: 0; right: 0; top: 615px; height: 109px;
  }
  .accreditations__badge {
    position: absolute;
    border-radius: 50%;
    border: 3px solid var(--badge-blue);
  }
  .badge--left { left: 34px; top: 16px; width: 88px; height: 88px; }
  .badge--right { left: 385px; top: 16px; width: 90px; height: 72px; }
  .accreditations__label {
    position: absolute;
    left: 146px; top: 14px;
    font-size: 10px;
    font-weight: 700;
    letter-spacing: 0.2px;
    color: var(--ink);
  }
  .card-slot {
    position: absolute;
    top: 32px;
    width: 96px; height: 62px;
    border: 2px solid var(--ink);
    background: var(--card-grey);
  }
  .card-slot--one { left: 146px; }
  .card-slot--two { left: 255px; }
</style>
</head>
<body>

<section class="leaflet leaflet--front" aria-label="Front – Domestic Cleaning">
  <svg class="leaflet__art" viewBox="0 0 512 724">
    <defs>
      <linearGradient id="bath" x1="0" y1="0" x2="1" y2="1">
        <stop offset="0" stop-color="var(--photo-bath-a)"/>
        <stop offset="1" stop-color="var(--photo-bath-b)"/>
      </linearGradient>
      <linearGradient id="person" x1="0" y1="0" x2="1" y2="1">
        <stop offset="0" stop-color="var(--photo-person-a)"/>
        <stop offset="1" stop-color="var(--photo-person-b)"/>
      </linearGradient>
      <linearGradient id="trolley" x1="0" y1="0" x2="0" y2="1">
        <stop offset="0" stop-color="var(--photo-trolley-a)"/>
        <stop offset="1" stop-color="var(--photo-trolley-b)"/>
      </linearGradient>
    </defs>
    <path role="img" aria-label="Photo: gloved hand spraying a bathroom sink and tap"
          d="M0 0 H512 V30 Q300 170 0 250 Z" fill="url(#bath)"/>
    <path role="img" aria-label="Photo: woman in yellow gloves wiping a kitchen worktop"
          d="M0 250 Q300 170 430 95 Q400 330 270 462 Q130 540 0 595 Z" fill="url(#person)"/>
    <path role="img" aria-label="Photo: cleaning trolley with buckets and supplies"
          d="M430 95 Q470 62 512 30 V400 Q380 420 270 462 Q400 330 430 95 Z" fill="url(#trolley)"/>
    <path d="M0 250 Q300 170 512 30" fill="none" stroke="var(--brand-blue)" stroke-width="7"/>
    <path d="M0 595 Q130 540 270 462 Q380 420 512 400" fill="none" stroke="var(--brand-blue)" stroke-width="7"/>
    <path d="M0 610 Q120 570 232 522" fill="none" stroke="var(--brand-blue)" stroke-width="2.5"/>
  </svg>

  <div class="brand"><span class="brand__dot"></span><span>Bright<br>Polish</span></div>

  <div class="service">
    <h2 class="service__title">Domestic Cleaning</h2>
    <ul class="service__list">
      <li class="service__item"><svg class="tick" viewBox="0 0 30 22"><ellipse cx="13" cy="13" rx="12" ry="7" fill="none" stroke="var(--brand-blue)" stroke-width="1.5"/><path d="M7 12 L12 18 L27 2" fill="none" stroke="var(--brand-blue)" stroke-width="3" stroke-linecap="round"/></svg><span>Weekly, fortnightly and<br>Monthly Cleaning Service</span></li>
      <li class="service__item"><svg class="tick" viewBox="0 0 30 22"><ellipse cx="13" cy="13" rx="12" ry="7" fill="none" stroke="var(--brand-blue)" stroke-width="1.5"/><path d="M7 12 L12 18 L27 2" fill="none" stroke="var(--brand-blue)" stroke-width="3" stroke-linecap="round"/></svg><span>Deep Blitz Cleaning</span></li>
      <li class="service__item"><svg class="tick" viewBox="0 0 30 22"><ellipse cx="13" cy="13" rx="12" ry="7" fill="none" stroke="var(--brand-blue)" stroke-width="1.5"/><path d="M7 12 L12 18 L27 2" fill="none" stroke="var(--brand-blue)" stroke-width="3" stroke-linecap="round"/></svg><span>Covered by a<br>Comprehensive Insurance</span></li>
    </ul>
  </div>

  <div class="call">
    <svg class="call__icon" viewBox="0 0 34 30"><ellipse cx="17" cy="17" rx="15" ry="9" fill="none" stroke="var(--brand-blue)" stroke-width="1.5"/><path d="M14 6 Q9 8 11 14 Q13 20 19 23 Q22 24 24 21 L21 18 L19 19 Q16 17 15 13 L17 11 Z" fill="var(--brand-blue)"/></svg>
    <span>Call Today!</span>
  </div>

  <div class="rule"></div>

  <div class="contact-bar">
    <span class="contact-bar__phone">01632 960 718</span>
    <span class="contact-bar__lines">info@brightpolishco.example<br>www.brightpolishco.example</span>
  </div>
</section>

<section class="leaflet leaflet--back" aria-label="Back – Carpet and Upholstery Cleaning">
  <svg class="leaflet__art" viewBox="0 0 512 724">
    <defs>
      <linearGradient id="carpet" x1="0" y1="0" x2="1" y2="1">
        <stop offset="0" stop-color="var(--photo-carpet-a)"/>
        <stop offset="1" stop-color="var(--photo-carpet-b)"/>
      </linearGradient>
      <linearGradient id="room" x1="0" y1="0" x2="1" y2="1">
        <stop offset="0" stop-color="var(--photo-room-b)"/>
        <stop offset="1" stop-color="var(--photo-room-a)"/>
      </linearGradient>
      <linearGradient id="child" x1="0" y1="0" x2="1" y2="1">
        <stop offset="0" stop-color="var(--photo-child-a)"/>
        <stop offset="1" stop-color="var(--photo-child-b)"/>
      </linearGradient>
    </defs>
    <path role="img" aria-label="Photo: gloved hands scrubbing a carpet stain with a sponge"
          d="M0 0 H440 Q400 80 330 130 Q160 70 0 75 Z" fill="url(#carpet)"/>
    <path role="img" aria-label="Photo: professional carpet cleaning machine in a living room"
          d="M0 75 Q160 70 330 130 Q360 190 344 251 Q112.5 270 0 390 Z" fill="url(#room)"/>
    <path role="img" aria-label="Photo: toddler crawling on a clean carpet"
          d="M440 0 H512 V250 Q421.5 245 344 251 Q360 190 330 130 Q400 80 440 0 Z" fill="url(#child)"/>
    <path d="M0 75 Q160 70 330 130" fill="none" stroke="var(--brand-blue)" stroke-width="6"/>
    <path d="M330 130 Q400 80 450 0" fill="none" stroke="var(--brand-blue)" stroke-width="5"/>
    <path d="M0 390 Q150 230 512 250" fill="none" stroke="var(--brand-blue)" stroke-width="7"/>
    <path d="M0 406 Q100 380 200 332" fill="none" stroke="var(--brand-blue)" stroke-width="2"/>
  </svg>

  <div class="service">
    <h2 class="service__title">Carpet and<br>Upholstery Cleaning</h2>
    <ul class="service__list">
      <li class="service__item"><svg class="tick" viewBox="0 0 30 22"><ellipse cx="13" cy="13" rx="12" ry="7" fill="none" stroke="var(--brand-blue)" stroke-width="1.5"/><path d="M7 12 L12 18 L27 2" fill="none" stroke="var(--brand-blue)" stroke-width="3" stroke-linecap="round"/></svg><span>Stain Removal Specialists</span></li>
      <li class="service__item"><svg class="tick" viewBox="0 0 30 22"><ellipse cx="13" cy="13" rx="12" ry="7" fill="none" stroke="var(--brand-blue)" stroke-width="1.5"/><path d="M7 12 L12 18 L27 2" fill="none" stroke="var(--brand-blue)" stroke-width="3" stroke-linecap="round"/></svg><span>Quick Drying Time</span></li>
      <li class="service__item"><svg class="tick" viewBox="0 0 30 22"><ellipse cx="13" cy="13" rx="12" ry="7" fill="none" stroke="var(--brand-blue)" stroke-width="1.5"/><path d="M7 12 L12 18 L27 2" fill="none" stroke="var(--brand-blue)" stroke-width="3" stroke-linecap="round"/></svg><span>Fresh Deodorising Finish</span></li>
      <li class="service__item"><svg class="tick" viewBox="0 0 30 22"><ellipse cx="13" cy="13" rx="12" ry="7" fill="none" stroke="var(--brand-blue)" stroke-width="1.5"/><path d="M7 12 L12 18 L27 2" fill="none" stroke="var(--brand-blue)" stroke-width="3" stroke-linecap="round"/></svg><span>Eco Friendly</span></li>
    </ul>
  </div>

  <div class="brand"><span class="brand__dot"></span><span>Bright<br>Polish</span></div>

  <div class="call">
    <svg class="call__icon" viewBox="0 0 34 30"><ellipse cx="17" cy="17" rx="15" ry="9" fill="none" stroke="var(--brand-blue)" stroke-width="1.5"/><path d="M14 6 Q9 8 11 14 Q13 20 19 23 Q22 24 24 21 L21 18 L19 19 Q16 17 15 13 L17 11 Z" fill="var(--brand-blue)"/></svg>
    <span>Call Today!</span>
  </div>

  <div class="rule"></div>

  <div class="contact-bar">
    <span class="contact-bar__phone">01632 960 718</span>
    <span class="contact-bar__lines">info@brightpolishco.example<br>www.brightpolishco.example</span>
  </div>

  <div class="accreditations">
    <div class="accreditations__badge badge--left" role="img" aria-label="Safety contractor accreditation badge"></div>
    <p class="accreditations__label">WE ACCEPT THESE MAJOR CREDIT CARDS</p>
    <div class="card-slot card-slot--one" role="img" aria-label="Accepted payment card"></div>
    <div class="card-slot card-slot--two" role="img" aria-label="Accepted payment card"></div>
    <div class="accreditations__badge badge--right" role="img" aria-label="Health and safety accredited contractor badge"></div>
  </div>
</section>

</body>
</html>
```